Stationary and envelopes

Need to have a new and edgy design for our stationary and matching envelopes. Check out our website at www.quillfordfieldservices.example

We do mainly construction and are the boots on the ground for the energy sector. I had you design our logo now next is stationary to make us stand out? ( boot print)

Target Market(s)

Corporate clients energy company

Font styles to use
Sans Serif

Requirements
Must have
• Logo and energy icons and what we do like the construction management and web address www.quillfordfieldservices.example
• Corporate office
• 48215 county road 92
• Harlow Bend, CO 80962
• 555.614.2873 ( office)
Nice to have
• Logo energy,icons web address corporate office Sterling colorado
• Do not just cut and paste the logo on white paper
Should not have
• Kiddy look imature look

```html
<!DOCTYPE html>
<html lang="en">
<head>
<meta charset="utf-8">
<title>Quillford Field Services – Business Card</title>
<link href="https://fonts.googleapis.com/css2?family=Roboto:wght@400;700&display=swap" rel="stylesheet">
<style>
  :root{
    --brown:#55231a;
    --navy:#0c1c3c;
    --card:#f4f4f4;
    --ink:#1d1d1d;
    --bg:#d6d6d6;
  }
  *{margin:0;padding:0;box-sizing:border-box}
  html,body{width:1200px;height:980px;overflow:hidden}
  body{background:var(--bg);font-family:"Roboto",Arial,sans-serif;color:var(--ink);position:relative}
  .card{position:absolute;left:303px;width:594px;height:330px;background:var(--card);overflow:hidden}
  .card--front{top:122px;border-top:6px solid var(--brown);border-bottom:6px solid var(--navy)}
  .card--back{top:528px}

  .holder{position:absolute;left:44px;top:72px}
  .holder__name{font-weight:700;font-size:19px;color:var(--brown);letter-spacing:.2px}
  .holder__title{font-size:13.5px;margin-top:4px}

  .wordmark{position:absolute;font-weight:700;color:var(--brown);text-align:center;line-height:1.05;text-transform:uppercase}
  .wordmark__main{display:block}
  .wordmark__sub{display:block;letter-spacing:2px}
  .card--front .wordmark{right:40px;top:56px;width:236px}
  .card--front .wordmark__main{font-size:38px;letter-spacing:1px}
  .card--front .wordmark__sub{font-size:16px;margin-top:5px;letter-spacing:3px}
  .card--back .wordmark{left:0;right:0;top:108px}
  .card--back .wordmark__main{font-size:48px;letter-spacing:2px}
  .card--back .wordmark__sub{font-size:20px;margin-top:6px;letter-spacing:4px}

  .contact{position:absolute;left:44px;top:225px;list-style:none;font-size:13.5px}
  .contact li{display:flex;align-items:center;height:18.5px}
  .contact svg{width:13px;height:13px;margin-right:9px;fill:none;stroke:var(--brown);stroke-width:1.4}
  .contact .solid{fill:var(--brown);stroke:none}

  .address{position:absolute;right:45px;top:243px;text-align:right;font-size:13.5px;line-height:18.5px}

  .sector-band{position:absolute;left:0;right:0;top:226px;height:66px;background:var(--navy);display:flex;justify-content:center;align-items:center;gap:22px}
  .sector-band svg{width:30px;height:38px;fill:none;stroke:#fff;stroke-width:1.8;stroke-linejoin:round;stroke-linecap:round}
  .web-band{position:absolute;left:0;right:0;top:292px;height:38px;background:var(--brown);color:#fff;font-size:14px;display:flex;align-items:center;justify-content:center}
</style>
</head>
<body>

<section class="card card--front">
  <div class="holder">
    <p class="holder__name">JORDAN PELLHAM</p>
    <p class="holder__title">General manager</p>
  </div>

  <p class="wordmark"><span class="wordmark__main">Quillford</span><span class="wordmark__sub">Field Services</span></p>

  <ul class="contact">
    <li><svg viewBox="0 0 14 14"><path class="solid" d="M3 1l2.5 3-1.3 1.5c.8 1.8 2 3 3.8 3.8L9.5 8l3 2.5-1.5 2C6.5 12.5 1.5 7.5 1.5 3z"/></svg>555.614.2873</li>
    <li><svg viewBox="0 0 14 14"><rect x="1" y="3" width="12" height="8"/><path d="M1 3l6 5 6-5"/></svg>info@quillfordfieldservices.example</li>
    <li><svg viewBox="0 0 14 14"><circle cx="7" cy="7" r="6"/><ellipse cx="7" cy="7" rx="2.6" ry="6"/><path d="M1 7h12M2 4h10M2 10h10"/></svg>www.quillfordfieldservices.example</li>
  </ul>

  <p class="address">48215 Cy Rd 92<br>Harlow Bend, CO 80962</p>
</section>

<section class="card card--back">
  <p class="wordmark"><span class="wordmark__main">Quillford</span><span class="wordmark__sub">Field Services</span></p>

  <div class="sector-band" aria-label="Energy sectors served">
    <svg viewBox="0 0 30 38"><path d="M15 3c2 7 9 11 9 20a9 9 0 0 1-18 0c0-5 3-8 5-11 0 4 2 6 4 6-2-5-1-10 0-15z"/></svg>
    <svg viewBox="0 0 30 38"><path d="M15 2L9 36M15 2l6 34M6 8h18M8 15h14M11 22l8 8M19 22l-8 8M4 8v3M26 8v3"/></svg>
    <svg viewBox="0 0 30 38"><path d="M5 6h20v28H5zM5 10h20"/><path d="M15 16c2 4 4 6 4 9a4 4 0 0 1-8 0c0-3 2-5 4-9z"/></svg>
    <svg viewBox="0 0 30 38"><path d="M15 14v22M12 36h6M15 14L15 2M15 14L5 20M15 14l10 6"/></svg>
    <svg viewBox="0 0 30 38"><circle cx="8" cy="9" r="3"/><path d="M8 2v2M2 9h2M3 4l1.5 1.5M13 4l-1.5 1.5M10 17l18 6-4 8L6 25zM17 28v8M13 36h8"/></svg>
    <svg viewBox="0 0 30 38"><rect x="12" y="3" width="6" height="7"/><path d="M15 10L6 36M15 10l9 26M15 10v26"/></svg>
  </div>
  <div class="web-band">www.quillfordfieldservices.example</div>
</section>

</body>
</html>
```